Lifestyle brand needs lip balm label design

We need a label design for lip balm tubes. The name of our company is "quorvalent"

Design Description:
Our lip balm tubes will be black. The label itself will be clear/transparent. We would like to create a gradient effect with the color green (same shade as our logo) starting from the bottom and slowly fading out to clear so that the black tube is visible (example of gradient shown in attached image)

We have two lip balm flavors: mint and lemongrass.
We would like the top/clear portion of the label to say "MINT" (all caps) . The second label should say "LEMONGRASS" (all caps) in the same location. Our logo "quorvalent" should be in the bottom/green portion of the label. Below the logo, we would like the words "NATURAL BALM" (all caps) in white text

```html
<!DOCTYPE html>
<html lang="en">
<head>
<meta charset="utf-8">
<title>quorvalent Natural Balm – Mint label</title>
<link rel="stylesheet" href="https://fonts.googleapis.com/css2?family=Jost:wght@300;400&display=swap">
<style>
  :root {
    --brand-green: #629a48;
    --accent-green: #6aa84f;
    --tint-green: #e6efdf;
    --ink: #1a1a1a;
    --paper: #ffffff;
    --page: #ffffff;
  }
  html, body {
    margin: 0;
    padding: 0;
    width: 908px;
    height: 1200px;
    overflow: hidden;
    background: var(--page);
  }
  .canvas {
    width: 908px;
    height: 1200px;
    display: flex;
    align-items: center;
    justify-content: center;
  }
  .label {
    display: block;
    width: 860px;
    height: 889px;
    box-shadow: 0 0 18px rgba(0, 0, 0, 0.28);
    background: var(--paper);
  }
  .label-text {
    font-family: "Jost", "Futura", sans-serif;
    text-anchor: middle;
  }
  .flavour-name {
    fill: var(--accent-green);
    font-weight: 300;
    font-size: 112px;
    letter-spacing: 14px;
  }
  .rule { stroke: var(--accent-green); stroke-width: 2; }
  .illustration-area { fill: var(--tint-green); }
  .body-copy {
    fill: var(--ink);
    font-weight: 400;
    font-size: 17px;
  }
  .brand-name {
    fill: var(--paper);
    font-weight: 300;
    font-size: 100px;
  }
  .product-name {
    fill: var(--paper);
    font-weight: 400;
    font-size: 38px;
    letter-spacing: 10px;
  }
  .fade-solid { stop-color: var(--brand-green); stop-opacity: 1; }
  .fade-clear { stop-color: var(--brand-green); stop-opacity: 0; }
</style>
</head>
<body>
<main class="canvas">
  <svg class="label" viewBox="0 0 807 834" xmlns="http://www.w3.org/2000/svg">
    <defs>
      <linearGradient id="bottom-fade" x1="0" y1="1" x2="0" y2="0">
        <stop offset="0" class="fade-solid"/>
        <stop offset="0.34" class="fade-solid"/>
        <stop offset="0.58" class="fade-clear"/>
        <stop offset="1" class="fade-clear"/>
      </linearGradient>
    </defs>

    <rect class="label-base" x="0" y="0" width="807" height="834" fill="var(--paper)"/>
    <rect class="label-fade" x="0" y="0" width="807" height="834" fill="url(#bottom-fade)"/>

    <text class="label-text flavour-name" x="410" y="150">MINT</text>
    <line class="rule rule--flavour" x1="353" y1="186" x2="453" y2="186"/>

    <rect class="illustration-area" x="318" y="214" width="170" height="170" rx="52"
          role="img" aria-label="Line drawing of a sprig of mint leaves in green"/>

    <text class="label-text body-copy" x="403" y="428">Lorem ipsum dolor sit amet, consectetuer</text>
    <text class="label-text body-copy" x="403" y="454">adipiscing elit, sed diam nonummy nibh</text>

    <text class="label-text brand-name" x="403" y="668">quorvalent</text>
    <text class="label-text product-name" x="408" y="746">NATURAL BALM</text>
  </svg>
</main>
</body>
</html>
```